Halvorsen Partners Business Card

Halvorsen Partners Civil Construction
Marcus Halvorsen
CEO
727-518-6094
Marcus@HalvorsenSiteworks.example
www.HalvorsenSiteworks.example
Site Development
Utility Construction
Excavation
40876 County Lane 19
Land O' Lakes, FL 34638

Target Market(s)

Construction and government

Industry/Entity Type

Business

Contact Information for Business Card

I want an unique design that make a statement

Number of Pages Required

1 page

Font styles to use

Colors

Designer to choose colors to be used in the design.

Requirements
Must have
• unique design, feel free to modify or change the color of my logo.
Nice to have
• extra design features like spot UV, foil accents, color edges, unique paper, or any thing that would make my card pop.
• I like the feel of the image that I attached

```html
<!DOCTYPE html>
<html lang="en">
<head>
<meta charset="utf-8">
<title>Halvorsen Partners Business Card</title>
<link rel="stylesheet" href="https://fonts.googleapis.com/css2?family=Open+Sans:wght@400;600&family=Tenor+Sans&display=swap">
<style>
  :root {
    --bg: #e9e7e3;
    --card-white: #ffffff;
    --card-black: #252525;
    --brand-blue: #1f3b8a;
    --brand-gray: #6b6c70;
    --ink: #1c1c1c;
    --white: #ffffff;
  }
  * { margin: 0; padding: 0; box-sizing: border-box; }
  html, body { width: 1200px; height: 900px; overflow: hidden; }
  body { background: var(--bg); position: relative; font-family: "Open Sans", sans-serif; }

  .card {
    position: absolute;
    width: 560px;
    height: 320px;
    overflow: hidden;
    box-shadow: 0 6px 18px rgba(0,0,0,0.18);
  }
  .card--back { left: 560px; top: 90px; background: var(--card-black); }
  .card--front { left: 80px; top: 470px; background: var(--card-white); }

  .card__shapes { position: absolute; inset: 0; }

  .brand {
    position: absolute;
    display: flex;
    align-items: center;
    gap: 12px;
    font-family: "Tenor Sans", sans-serif;
    letter-spacing: 1px;
    text-transform: uppercase;
    white-space: nowrap;
  }
  .brand__square { width: 22px; height: 22px; }
  .card--back .brand { left: 50%; top: 50%; transform: translate(-50%, -50%); color: var(--white); font-size: 30px; }
  .card--back .brand__square { background: var(--white); }
  .card--front .brand { left: 170px; top: 122px; color: var(--brand-blue); font-size: 26px; }
  .card--front .brand__square { background: var(--brand-blue); }

  .person { position: absolute; left: 62px; top: 14px; }
  .person__name { font-family: "Tenor Sans", sans-serif; color: var(--brand-blue); font-size: 19px; letter-spacing: 0.5px; text-transform: uppercase; }
  .person__role { font-size: 11px; color: var(--ink); margin-top: -2px; }

  .contact { position: absolute; left: 22px; top: 170px; list-style: none; font-size: 12.5px; color: var(--ink); }
  .contact li { display: flex; align-items: center; gap: 7px; line-height: 17px; }
  .contact svg { width: 11px; height: 11px; fill: var(--brand-blue); flex: none; }

  .services { position: absolute; right: 22px; top: 206px; list-style: none; text-align: right; font-size: 15px; color: var(--ink); }
  .services li { line-height: 19px; display: flex; justify-content: flex-end; align-items: center; gap: 8px; }
  .services li::after { content: ""; width: 8px; height: 8px; border-radius: 50%; background: var(--brand-blue); }
</style>
</head>
<body>

<section class="card card--back" aria-label="Card back">
  <div class="brand">
    <span class="brand__square"></span>
    <span class="brand__name">Halvorsen Partners</span>
  </div>
</section>

<section class="card card--front" aria-label="Card front">
  <svg class="card__shapes" viewBox="0 0 560 320" aria-hidden="true">
    <polygon points="0,0 42,0 0,34" fill="var(--brand-blue)"/>
    <polygon points="50,0 60,0 40,40 22,40" fill="var(--brand-gray)"/>
    <polygon points="0,232 214,280 204,300 0,254" fill="var(--brand-blue)"/>
    <polygon points="224,282 560,282 560,308 214,308" fill="var(--brand-gray)"/>
  </svg>

  <div class="person">
    <div class="person__name">Marcus Halvorsen</div>
    <div class="person__role">CEO</div>
  </div>

  <div class="brand">
    <span class="brand__square"></span>
    <span class="brand__name">Halvorsen Partners</span>
  </div>

  <ul class="contact">
    <li><svg viewBox="0 0 24 24"><path d="M6.6 10.8a15 15 0 0 0 6.6 6.6l2.2-2.2a1 1 0 0 1 1-.25 11.4 11.4 0 0 0 3.6.57 1 1 0 0 1 1 1V20a1 1 0 0 1-1 1A17 17 0 0 1 3 4a1 1 0 0 1 1-1h3.5a1 1 0 0 1 1 1c0 1.25.2 2.45.57 3.6a1 1 0 0 1-.25 1z"/></svg>727-518-6094</li>
    <li><svg viewBox="0 0 24 24"><path d="M2 5h20v14H2z M2 5l10 8 10-8" stroke="#fff" stroke-width="1.5"/></svg>Marcus@HalvorsenSiteworks.example</li>
    <li><svg viewBox="0 0 24 24"><circle cx="12" cy="12" r="10"/></svg>www.HalvorsenSiteworks.example</li>
  </ul>

  <ul class="services">
    <li>Site Development</li>
    <li>Utility Construction</li>
    <li>Excavation</li>
  </ul>
</section>

</body>
</html>
```